Church needs a graphic design/flyer layout for upcoming series

I need a multi-purpose design for promoting both our upcoming series of messages and our fall kick-off event where we will launch the messages.

Our promotion will be printed on a two-sided. One side is simple and focuses on the series and the other side has details in regards to the event. I have provided an attachment example of what we did last time.

The design needs to be multi-purpose because it will be used for our sermon Power Points, placed on our website banner, social media, etc.

• Sermon series is called “Harbor Lanterns”
• The subtitle will be “What’s keeping you from God?”
• Our name logo should be on the graphic as well.
• The subject manner will revolve around common hurdles that people face about God and Christianity: The existence of God, the exclusivity of religion, Hell, the reliability of the Bible, Hypocrisy in the church, etc.
• Our mission is “Connecting Young Families to Christ” so our focus is to reach out to families while not being exclusive to others.
• Our target audience is families with school-aged kids.
• This series is an invitational focus so we want it to be appealing to non-church goers.
• It should be attention grabbing while not being too ‘edgy’

• The front of the card will most likely consist the Sermon Series Graphic, title & subtitle of the series, and perhaps our name logo somewhere on it.
• The back of the card will invite and give the basic information for the event so that the people will be encouraged to save the date and come to the event.
• Here are some things that could be included on that advertisement:
o The name of the event: “Westbrook Commons Open Day”
o The date and time of the event: Sept 23rd @ 10:30
o Features of the event:
 Free lunch
 Children’s program
 Bouncy Castle
 Start of the “Harbor Lanterns” messages.
 Sample of topics
o Information about the church: our website and address, etc
o Engaging pictures and graphics.
• The rest of the tone and manner are the same as the sermon series graphic.
The flyer will be 11X14, like a postcard size.

Target Market(s)

Young families who are spiritually curious but not committed church attenders.

Colors

Designer to choose colors to be used in the design.

Requirements
Nice to have
• A modern and professional looking design.
Should not have
• Anything offensive or not family friendly.

```html
<!DOCTYPE html>
<html lang="en">
<head>
<meta charset="utf-8">
<title>Harbor Lanterns – Westbrook Commons Open Day</title>
<link href="https://fonts.googleapis.com/css2?family=Merriweather:wght@900&family=Lato:wght@300;400&family=Tinos:wght@400;700&display=swap" rel="stylesheet">
<style>
  :root {
    --backdrop: #cfcfcf;
    --orange: #f39220;
    --blue: #1f75be;
    --purple: #8e2a8e;
    --ink: #222222;
    --white: #ffffff;
  }
  * { margin: 0; padding: 0; box-sizing: border-box; }
  html, body { width: 1200px; height: 1200px; overflow: hidden; background: var(--backdrop); }
  .canvas { position: relative; width: 1200px; height: 1200px; }

  .card { position: absolute; left: 270px; width: 661px; overflow: hidden; }
  .card--front { top: 58px; height: 519px; }
  .card--back { top: 622px; height: 520px; }

  .hero-photo {
    position: absolute; inset: 0;
    background:
      radial-gradient(ellipse 40% 55% at 85% 100%, rgba(20,16,14,.95), rgba(20,16,14,0) 100%),
      radial-gradient(ellipse 30% 12% at 50% 48%, rgba(255,170,60,.9), rgba(255,170,60,0) 100%),
      linear-gradient(180deg, #b9c6cf 0%, #d8cdb8 22%, #f2b869 40%, #f49a3a 48%, #6c7787 52%, #a9b1bb 62%, #7d8591 78%, #3c3a3c 100%);
  }

  .frame { position: absolute; left: 38px; top: 38px; width: 586px; height: 444px; }
  .card--front .frame { border: 1.5px solid var(--purple); }
  .card--back .frame { border: 1.5px solid var(--white); }

  .brand-name {
    position: absolute; display: flex; align-items: center; gap: 8px;
    font-family: "Lato", sans-serif; font-weight: 300; color: var(--ink);
  }
  .brand-name .dot { width: 14px; height: 14px; border-radius: 50%; background: var(--orange); }
  .card--front .brand-name { left: 52px; top: 114px; font-size: 14px; }

  .series-title {
    position: absolute; right: 61px; top: 382px;
    font-family: "Merriweather", serif; font-weight: 900; font-size: 33px;
    color: var(--orange); white-space: nowrap;
  }
  .series-subtitle {
    position: absolute; right: 61px; top: 426px;
    font-family: "Lato", sans-serif; font-weight: 300; font-size: 28px;
    color: var(--white); white-space: nowrap; letter-spacing: .5px;
  }

  .back-texture {
    position: absolute; inset: 0;
    background: linear-gradient(135deg, #e4e3e3 0%, #f6f6f6 35%, #dedddd 60%, #f3f3f3 100%);
  }
  .back-content { position: absolute; inset: 0; text-align: center; font-family: "Tinos", serif; color: var(--ink); }

  .event-title {
    position: absolute; left: 0; right: 0; top: 52px;
    font-family: "Merriweather", serif; font-weight: 900; font-size: 31px; color: var(--blue);
  }
  .event-when {
    position: absolute; left: 0; right: 0; top: 96px;
    display: flex; justify-content: center; align-items: center; gap: 28px;
    font-weight: 700; font-size: 24px;
  }
  .event-when span { display: flex; align-items: center; gap: 10px; }

  .features-heading {
    position: absolute; left: 0; right: 0; top: 150px;
    display: flex; justify-content: center; align-items: center; gap: 12px;
    font-weight: 700; font-size: 29px; color: var(--blue);
  }
  .features-heading::before, .features-heading::after {
    content: ""; width: 52px; height: 2px; background: var(--white);
  }

  .feature-row {
    position: absolute; left: 0; right: 0;
    display: flex; justify-content: center; list-style: none;
    font-size: 18px;
  }
  .feature-row--1 { top: 200px; gap: 38px; }
  .feature-row--2 { top: 238px; gap: 40px; }
  .feature-row li::before { content: "•"; color: var(--purple); margin-right: 10px; }

  .card--back .brand-name { left: 0; right: 0; top: 366px; justify-content: center; font-size: 17px; }

  .contact-row {
    position: absolute; left: 0; right: 0; top: 414px;
    display: flex; justify-content: center; align-items: center; gap: 14px; font-size: 13px;
  }
  .contact-row span { display: flex; align-items: center; gap: 7px; }
  .contact-row .phone { font-weight: 700; font-size: 19px; }
  .address {
    position: absolute; left: 0; right: 0; top: 444px;
    display: flex; justify-content: center; align-items: center; gap: 4px; font-size: 14px;
  }
  svg.icon { fill: none; stroke: var(--purple); stroke-width: 2; }
</style>
</head>
<body>
<div class="canvas">

  <section class="card card--front">
    <div class="hero-photo" role="img" aria-label="Photo: person with raised arms on a mountain peak above a sea of clouds at sunrise"></div>
    <div class="frame"></div>
    <div class="brand-name"><i class="dot"></i>Maple Hollow Family Church</div>
    <h1 class="series-title">Harbor Lanterns</h1>
    <p class="series-subtitle">What’s keeping you from God?</p>
  </section>

  <section class="card card--back">
    <div class="back-texture" role="img" aria-label="Soft light grey faceted background texture"></div>
    <div class="frame"></div>
    <div class="back-content">
      <h2 class="event-title">Westbrook Commons Open Day</h2>
      <div class="event-when">
        <span>
          <svg class="icon" width="18" height="18" viewBox="0 0 18 18"><rect x="2" y="3.5" width="14" height="12.5" rx="1"/><line x1="2" y1="7.5" x2="16" y2="7.5"/><line x1="5.5" y1="1.5" x2="5.5" y2="5"/><line x1="12.5" y1="1.5" x2="12.5" y2="5"/></svg>
          September 23rd
        </span>
        <span>
          <svg class="icon" width="26" height="26" viewBox="0 0 26 26"><circle cx="13" cy="13" r="11"/><polyline points="13,6 13,13 18,13"/></svg>
          10:30 am
        </span>
      </div>
      <h3 class="features-heading">Features of the event</h3>
      <ul class="feature-row feature-row--1">
        <li>Free lunch</li>
        <li>Children’s program</li>
        <li>Bouncy Castle</li>
      </ul>
      <ul class="feature-row feature-row--2">
        <li>Start of the “Harbor Lanterns” messages.</li>
        <li>Sample of topics</li>
      </ul>

      <div class="brand-name"><i class="dot"></i>Maple Hollow Family Church</div>

      <div class="contact-row">
        <span class="phone">
          <svg class="icon" width="19" height="19" viewBox="0 0 20 20"><circle cx="10" cy="10" r="8.5"/><path d="M7 6 l2 2 -1 1.5 q1 2 2.5 2.5 l1.5 -1 2 2 -1.5 1.5 q-4 -.5 -6.5 -6.5z"/></svg>
          905.555.0142
        </span>
        <span>
          <svg class="icon" width="19" height="13" viewBox="0 0 20 14"><rect x="1" y="1" width="18" height="12"/><polyline points="1,1 10,8 19,1"/></svg>
          info@maplehollowchurch.ca
        </span>
        <span>
          <svg class="icon" width="18" height="18" viewBox="0 0 20 20"><circle cx="10" cy="10" r="8.5"/><ellipse cx="10" cy="10" rx="4" ry="8.5"/><line x1="1.5" y1="10" x2="18.5" y2="10"/></svg>
          www.maplehollowchurch.ca
        </span>
      </div>
      <div class="address">
        <svg width="10" height="14" viewBox="0 0 10 14"><path d="M5 0a5 5 0 0 1 5 5c0 4-5 9-5 9S0 9 0 5a5 5 0 0 1 5-5z" fill="#8e2a8e"/><circle cx="5" cy="5" r="1.8" fill="#fff"/></svg>
        1180 Cedar Ridge Road, Oakfield, ON K2A 0B4
      </div>
    </div>
  </section>

</div>
</body>
</html>
```